Vornel Technologies business card design

We need a business card designed with our new logo. it would be great if the card could communicate it is a technology based company.

Target Market(s)

system integrators

Industry/Entity Type

technology, IOT

Contact Information for Business Card

Name, designation, Address, telephone number, email address

Requirements
Must have
• logo and company name
Nice to have
• something to do with technology

```html
<!DOCTYPE html>
<html lang="en">
<head>
<meta charset="utf-8">
<title>Vornel Technologies — Business Card</title>
<link rel="stylesheet" href="https://fonts.googleapis.com/css2?family=Roboto:wght@400;500;700&display=swap">
<style>
  :root {
    --page-bg: #ececec;
    --card-top: #1d1d1d;
    --card-bottom: #0b0b0b;
    --accent: #f7941d;
    --text-light: #ffffff;
    --faint-grey: rgba(255,255,255,0.12);
    --faint-orange: rgba(247,148,29,0.14);
  }
  * { margin: 0; padding: 0; box-sizing: border-box; }
  html, body { width: 1200px; height: 2922px; overflow: hidden; background: var(--page-bg); }
  body { font-family: "Roboto", Arial, sans-serif; position: relative; }

  .card {
    position: absolute;
    left: 157px;
    width: 930px;
    height: 530px;
    background: linear-gradient(160deg, var(--card-top) 0%, var(--card-bottom) 75%);
    box-shadow: 0 18px 40px rgba(0,0,0,0.28);
    overflow: hidden;
  }
  .card--front { top: 900px; }
  .card--back { top: 1492px; }

  .brand {
    position: absolute;
    display: flex;
    align-items: center;
    gap: 14px;
  }
  .brand__square { width: 22px; height: 22px; background: var(--accent); transform: rotate(45deg); }
  .brand__name {
    font-weight: 500;
    font-size: 38px;
    color: var(--text-light);
    letter-spacing: 0.5px;
    white-space: nowrap;
  }
  .card--front .brand { left: 126px; top: 130px; }
  .card--back .brand { left: 336px; top: 238px; }

  .contact { position: absolute; left: 130px; top: 316px; color: var(--text-light); }
  .contact__name { font-weight: 500; font-size: 25px; margin-bottom: 20px; }
  .contact__row { display: flex; align-items: center; gap: 14px; font-size: 18px; margin-bottom: 12px; }
  .contact__icon { width: 28px; height: 28px; flex: none; }

  .decor { position: absolute; }
  .card--front .decor { right: -20px; top: 160px; width: 320px; height: 320px; }
  .card--back .decor { left: 30px; top: 160px; width: 330px; height: 330px; }
</style>
</head>
<body>

<section class="card card--front" aria-label="Business card front">
  <div class="brand">
    <span class="brand__square"></span>
    <span class="brand__name">Vornel Technologies</span>
  </div>

  <div class="contact">
    <p class="contact__name">NAME</p>
    <p class="contact__row">
      <svg class="contact__icon" viewBox="0 0 28 28" aria-hidden="true">
        <rect x="5" y="5" width="18" height="18" transform="rotate(45 14 14)" fill="var(--accent)"/>
        <path d="M10.5 9.5 l2 0 l1 2.5 l-1.3 1 a6 6 0 0 0 2.8 2.8 l1-1.3 l2.5 1 l0 2 a1.5 1.5 0 0 1-1.6 1.3 a9 9 0 0 1-7.7-7.7 a1.5 1.5 0 0 1 1.3-1.6z" fill="#fff"/>
      </svg>
      <span>1234567890</span>
    </p>
    <p class="contact__row">
      <svg class="contact__icon" viewBox="0 0 28 28" aria-hidden="true">
        <rect x="5" y="5" width="18" height="18" transform="rotate(45 14 14)" fill="var(--accent)"/>
        <rect x="9" y="10.5" width="10" height="7" fill="none" stroke="#fff" stroke-width="1.4"/>
        <path d="M9 10.5 l5 4 l5-4" fill="none" stroke="#fff" stroke-width="1.4"/>
      </svg>
      <span>www.yourmailthere@vornelmail.com</span>
    </p>
  </div>

  <svg class="decor" viewBox="0 0 320 320" aria-hidden="true">
    <rect x="40" y="40" width="220" height="220" transform="rotate(30 150 150)" fill="var(--faint-grey)"/>
    <rect x="150" y="10" width="150" height="150" transform="rotate(30 225 85)" fill="var(--faint-orange)"/>
  </svg>
</section>

<section class="card card--back" aria-label="Business card back">
  <svg class="decor" viewBox="0 0 330 330" aria-hidden="true">
    <rect x="30" y="60" width="220" height="220" transform="rotate(30 140 170)" fill="var(--faint-grey)"/>
    <rect x="130" y="20" width="150" height="150" transform="rotate(30 205 95)" fill="var(--faint-orange)"/>
  </svg>

  <div class="brand">
    <span class="brand__square"></span>
    <span class="brand__name">Vornel Technologies</span>
  </div>
</section>

</body>
</html>
```